Flyer
Zielgruppe
Ich bin Energieberater für Wohngebäude. Ich möchte ein Flyer über meine Leistungen erstellen. Dabei möchte ich gezielt potentielle Partner wie Architekten und Immobilienverwalter ansprechen und ein Netzwerk aufbauen.
Meine Leistungen im Überblick:
- Energieberatung
- Individueller Sanierungsfahrplan (iSFP)
- Energieausweise
- TbH-Effizienzhaus-Planung (Neubau und Bestand)
- Planung klimafreundlicher Neubau (KFN)
- Fördermittelberatung und -beantragung
- PUL-Einzelmaßnahmen wie z. B. Dämmung der Gebäudehülle oder Fenstertausch uvm.
- Heizlastberechnung nach DIN EN 12831
- Hydraulischer Abgleich nach Verfahren A/B
- Heizflächenauslegung
- Wärmepumpen (Beratung und Auslegung)
Meine Signatur:
M. Eng. Torben Wiskow
Energieberater / Planungsingenieur
Volmar Haus
Lindholzgasse 7C
47263 Ostwalden
Tel: 0152 / 871 43 06
E-Mail: info@Volmar-Haus.de
Aufgabenstellung
Ich möchte den Flyer sowohl als PDF-Format nutzen, um Kalt-Akquise übers Internet zu betreiben, als auch ausgedruckt.

```html
<!DOCTYPE html>
<html lang="de">
<head>
<meta charset="utf-8">
<title>Volmar Haus – Flyer</title>
<link rel="stylesheet" href="https://fonts.googleapis.com/css2?family=Montserrat:wght@400;500;600;700;800;900&display=swap">
<style>
  :root {
    --stage: #ebebeb;
    --paper: #f6f6f6;
    --ink: #141414;
    --blue: #2f72c0;
    --blue-band: #3578c4;
    --teal: #2fc1c4;
    --green: #2eb34f;
    --muted: #6d625b;
    --sky-top: #cfe2f4;
    --sky-low: #eaf2fa;
  }
  * { box-sizing: border-box; margin: 0; padding: 0; }
  html, body { width: 1200px; height: 800px; overflow: hidden; }
  body {
    background: var(--stage);
    font-family: "Montserrat", sans-serif;
    color: var(--ink);
    position: relative;
  }
  .flyer {
    position: absolute;
    top: 46px;
    width: 500px;
    height: 707px;
    background: var(--paper);
    overflow: hidden;
    box-shadow: 0 10px 30px rgba(0,0,0,.12);
  }
  .flyer--services { left: 80px; }
  .flyer--cover { left: 620px; }

  /* Services page */
  .services-title {
    position: absolute; top: 52px; left: 0; width: 100%;
    text-align: center; font-weight: 900; font-size: 33px; letter-spacing: .5px;
  }
  .services-title .accent { color: var(--blue); }
  .service-list {
    position: absolute; top: 128px; list-style: none;
    font-size: 13px; font-weight: 500; line-height: 1.35;
  }
  .service-list--left { left: 46px; width: 200px; }
  .service-list--right { left: 262px; width: 200px; }
  .service-list li { position: relative; padding-left: 26px; margin-bottom: 12px; }
  .service-list li::before {
    content: ""; position: absolute; left: 4px; top: 1px;
    width: 7px; height: 13px;
    border-right: 3px solid var(--green); border-bottom: 3px solid var(--green);
    transform: rotate(40deg);
  }
  .energy-visual {
    position: absolute; left: 150px; top: 440px; width: 350px; height: 150px;
    background: linear-gradient(100deg, rgba(246,246,246,0) 0%, #d8e6ef 25%, #cde3b4 50%, #f0dc95 70%, #f1b59b 85%, rgba(246,246,246,0) 100%);
    opacity: .75;
  }
  .portrait {
    position: absolute; z-index: 2;
    background: linear-gradient(180deg, #d9d0c8 0%, #c9a994 28%, #f1f1f1 48%, #2b3448 62%, #243045 100%);
  }
  .flyer--services .portrait { left: 30px; top: 520px; width: 190px; height: 187px; }
  .signature { position: absolute; z-index: 2; font-size: 12.5px; line-height: 1.4; }
  .signature .name { color: var(--blue); font-weight: 700; }
  .signature .role { font-weight: 700; }
  .flyer--services .signature { left: 232px; top: 552px; }
  .teal-line { position: absolute; z-index: 1; left: 0; width: 100%; height: 5px; background: var(--teal); }
  .contact-band {
    position: absolute; z-index: 1; left: 0; bottom: 0; width: 100%;
    background: var(--blue-band); color: #fff;
  }
  .flyer--services .teal-line { top: 595px; }
  .flyer--services .contact-band { top: 604px; }
  .contact { position: absolute; text-align: right; }
  .flyer--services .contact { right: 26px; top: 16px; }
  .phone { display: flex; align-items: center; justify-content: flex-end; gap: 8px; font-size: 26px; font-weight: 700; }
  .phone svg { width: 20px; height: 20px; }
  .web { font-size: 15px; font-weight: 700; letter-spacing: .5px; margin-top: 2px; }
  .address { font-size: 8px; font-weight: 600; letter-spacing: .4px; margin-top: 4px; }

  /* Cover page */
  .cover-sky {
    position: absolute; inset: 0 0 auto 0; height: 430px;
    background: linear-gradient(180deg, var(--sky-top) 0%, var(--sky-low) 55%, var(--paper) 100%);
  }
  .cover-title {
    position: absolute; top: 46px; left: 0; width: 100%; text-align: center;
    font-weight: 900; font-size: 30px; line-height: 1.15; letter-spacing: .3px;
  }
  .cover-title .accent { color: var(--blue); }
  .house-photo {
    position: absolute; left: 0; top: 170px; width: 100%; height: 260px;
    background: linear-gradient(180deg, rgba(255,255,255,0) 0%, #e9eef2 20%, #9ea4a8 45%, #6e8a5e 70%, rgba(246,246,246,0) 100%);
  }
  .brand {
    position: absolute; left: 300px; top: 400px; width: 170px; text-align: center;
  }
  .brand-dot {
    width: 82px; height: 82px; border-radius: 50%; background: #fff;
    margin: 0 auto 12px; box-shadow: 0 0 0 14px rgba(255,255,255,.6);
  }
  .brand-name { font-size: 16px; font-weight: 600; color: var(--muted); letter-spacing: 1px; }
  .brand-tag { font-size: 7.5px; font-weight: 500; color: var(--muted); margin-top: 2px; }
  .flyer--cover .portrait { left: 0; top: 440px; width: 210px; height: 267px; }
  .flyer--cover .signature { left: 220px; top: 540px; }
  .flyer--cover .teal-line { top: 600px; }
  .flyer--cover .contact-band { top: 609px; }
  .flyer--cover .contact { right: 22px; top: 14px; }
</style>
</head>
<body>

<section class="flyer flyer--services" aria-label="Flyer Rückseite: Leistungen">
  <h2 class="services-title">UNSERE <span class="accent">LEISTUNGEN</span></h2>
  <ul class="service-list service-list--left">
    <li>Energieberatung</li>
    <li>Individueller Sanierungsfahrplan (iSFP)</li>
    <li>Energieausweise</li>
    <li>TbH-Effizienzhaus-Planung (Neubau und Bestand)</li>
    <li>Planung klimafreundlicher Neubau (KFN)</li>
    <li>Fördermittelberatung und -beantragung</li>
  </ul>
  <ul class="service-list service-list--right">
    <li>PUL-Einzelmaßnahmen wie z. B. Dämmung der Gebäudehülle oder Fenstertausch uvm.</li>
    <li>Heizlastberechnung nach DIN EN 12831</li>
    <li>Hydraulischer Abgleich nach Verfahren A/B</li>
    <li>Heizflächenauslegung</li>
    <li>Wärmepumpen (Beratung und Auslegung)</li>
  </ul>
  <div class="energy-visual" role="img" aria-label="Hausmodell auf Bauplänen mit Energieeffizienzskala"></div>
  <div class="portrait" role="img" aria-label="Porträtfoto des Energieberaters im dunklen Sakko"></div>
  <div class="signature">
    <div class="name">M. Eng. Torben Wiskow</div>
    <div class="role">Energy consultant / planning engineer</div>
  </div>
  <div class="teal-line"></div>
  <div class="contact-band">
    <div class="contact">
      <div class="phone">
        <svg viewBox="0 0 24 24" aria-hidden="true"><path fill="#fff" d="M6.6 10.8a15.1 15.1 0 0 0 6.6 6.6l2.2-2.2c.3-.3.7-.4 1-.2 1.1.4 2.3.6 3.6.6.6 0 1 .4 1 1V20c0 .6-.4 1-1 1A17 17 0 0 1 3 4c0-.6.4-1 1-1h3.5c.6 0 1 .4 1 1 0 1.3.2 2.5.6 3.6.1.3 0 .7-.2 1z"/></svg>
        0152/8714306
      </div>
      <div class="web">WWW.VOLMAR-HAUS.DE</div>
      <div class="address">LINDHOLZGASSE 7C | 47263 OSTWALDEN</div>
    </div>
  </div>
</section>

<section class="flyer flyer--cover" aria-label="Flyer Vorderseite">
  <div class="cover-sky"></div>
  <h1 class="cover-title">INGENIEURTECHNISCHE<br>PLANUNG IN DER<br><span class="accent">ENERGIEWENDE!</span></h1>
  <div class="house-photo" role="img" aria-label="Modernes weißes Einfamilienhaus mit Solaranlage auf dem Dach"></div>
  <div class="brand">
    <div class="brand-dot"></div>
    <div class="brand-name">VOLMAR HAUS</div>
    <div class="brand-tag">Planung, Berechnung, Auslegung</div>
  </div>
  <div class="portrait" role="img" aria-label="Porträtfoto des Energieberaters im dunklen Sakko"></div>
  <div class="signature">
    <div class="name">M. Eng. Torben Wiskow</div>
    <div class="role">Energy consultant / planning engineer</div>
  </div>
  <div class="teal-line"></div>
  <div class="contact-band">
    <div class="contact">
      <div class="phone">
        <svg viewBox="0 0 24 24" aria-hidden="true"><path fill="#fff" d="M6.6 10.8a15.1 15.1 0 0 0 6.6 6.6l2.2-2.2c.3-.3.7-.4 1-.2 1.1.4 2.3.6 3.6.6.6 0 1 .4 1 1V20c0 .6-.4 1-1 1A17 17 0 0 1 3 4c0-.6.4-1 1-1h3.5c.6 0 1 .4 1 1 0 1.3.2 2.5.6 3.6.1.3 0 .7-.2 1z"/></svg>
        0152/8714306
      </div>
      <div class="web">WWW.VOLMAR-HAUS.DE</div>
      <div class="address">LINDHOLZGASSE 7C | 47263 OSTWALDEN</div>
    </div>
  </div>
</section>

</body>
</html>
```